Managed IT Service Provider Needs a Slick "Who We Are" or "Intro" Brochure

http://www.brellix.com/

tag line: Smart Network Solutions
Mission statement: Accelerating business through technology

We need a basic intro brochure that is snazzy, modern, and clean. It will not be a text heavy document. It needs to primarily introduce us, and discuss roughly our managed service offerings which we call "Calm Shield".

Once this intro doc is complete, we would like to work with the designer to complete some more product specific documents with the same look and feel. We are also interested in a matching business card design.

Here's a design we ran across and liked it: http://www.artbidhub.com/design/3849126

The design above has roughly the amount of text we'd like to see. It's clean, modern and fun. This is just an example of something we liked. Clean designs are great, not too busy.

It should talk about reliability, our professionalism, and our vigilance. We are stewards of information for our clients. This brochure doesn't need to provide a ton of information about our services, but should essentially be a call-to-action to contact us if you have a small to medium business and need a reliable technology partner to guide you.

Here's some older text:

Brellix is a leading edge Information Technology (IT) services company providing innovative solutions to all forms of IT challenges for small, medium and enterprise sized clients. Brellix has performed technology services in a multitude of industries including law enforcement, government, healthcare, educational, financial, broadcast and others. As a full service integrator, Brellix provides network design, installation, maintenance, and administration. Whether you are a client who uses our Managed Services offerings or our Consulting Services, you can expect Brellix’s certified professionals to achieve the best possible network performance, security and reliability using the most expeditious and cost effective methods available.

Some pics of our vans, an older capability doc (rough draft), and our logo in vector format is attached.

We are looking for something that flows with our website and vans.

We have a max of 5 days for this before we need to get them to the local printer for next Friday evening.

Target Market(s)

Small and Medium Business - Medical, Law, Engineering, Financial, other professional services firms.

Industry/Entity Type

Business

Contact Information for Business Card

Just looking for something that matches the doc design. Clean modern card. Should have our mission, maybe on the back: Accelerating business through technology

Font styles to use
Sans Serif

Requirements
Must have
• Modern tech design. Should flow with our website and van colors.
• I should add we are looking for a single 8.5" x 11" page, front and back, oriented vertically. We do not intend on folding this in any way. It will be inserted into a presentation folder with other materials.

```html
<!DOCTYPE html>
<html lang="en">
<head>
<meta charset="utf-8">
<title>Brellix – Who We Are</title>
<link href="https://fonts.googleapis.com/css2?family=Open+Sans:wght@400;600;700&display=swap" rel="stylesheet">
<style>
  :root {
    --brand-blue: #1c7fc4;
    --deep-navy: #0f2a44;
    --ink: #2f3a44;
    --muted: #5b6670;
    --paper: #ffffff;
    --mist: #e9f3fa;
  }
  * { margin: 0; padding: 0; box-sizing: border-box; }
  html, body { width: 829px; height: 1200px; overflow: hidden; background: var(--paper); }
  body { font-family: "Open Sans", Arial, sans-serif; color: var(--ink); }

  .flyer {
    position: relative; width: 829px; height: 1200px; background: var(--paper);
    display: flex; flex-direction: column;
  }

  .masthead {
    flex: 0 0 150px; display: flex; align-items: center; justify-content: space-between;
    padding: 0 56px;
  }
  .brand { display: flex; align-items: center; gap: 16px; }
  .brand-dot { width: 44px; height: 44px; border-radius: 50%; background: var(--brand-blue); }
  .brand-name { font-size: 52px; font-weight: 600; color: var(--deep-navy); line-height: 1; letter-spacing: -1px; }
  .brand-tag { font-size: 17px; color: var(--brand-blue); margin-top: 4px; margin-left: 60px; }
  .contact { font-size: 22px; color: var(--deep-navy); line-height: 1.55; }
  .contact div { display: flex; align-items: center; gap: 10px; }
  .contact svg { width: 20px; height: 20px; fill: var(--brand-blue); }

  .hero {
    position: relative; flex: 0 0 470px;
    background: radial-gradient(ellipse at 35% 40%, #6fa3c8 0%, #2f5f85 40%, #132c45 85%);
  }
  .hero-tagline {
    position: absolute; right: 44px; bottom: 36px; text-align: right;
    color: #fff; font-size: 33px; line-height: 1.25;
  }
  .hero-tagline strong { font-weight: 700; }

  .intro { flex: 0 0 auto; padding: 28px 56px 0; }
  .intro h2 { color: var(--brand-blue); font-size: 28px; font-weight: 700; margin-bottom: 10px; line-height: 1.2; }
  .intro p { font-size: 14.5px; line-height: 1.4; color: var(--muted); margin-bottom: 12px; }
  .intro p:last-child { margin-bottom: 0; }
  .intro .accent { color: var(--brand-blue); font-weight: 600; }

  .closing {
    position: relative; flex: 1 1 auto;
    padding: 30px 56px 0;
    background: linear-gradient(180deg, var(--paper) 0%, var(--mist) 55%, #cfe4f3 100%);
  }
  .closing p { font-size: 22px; line-height: 1.4; color: var(--ink); margin-bottom: 18px; }
  .closing .accent { color: var(--brand-blue); font-weight: 600; }
  .closing svg { position: absolute; left: 0; bottom: 0; }
</style>
</head>
<body>
<main class="flyer">
  <header class="masthead">
    <div>
      <div class="brand">
        <span class="brand-dot"></span>
        <span class="brand-name">brellix</span>
      </div>
      <div class="brand-tag">smart network solutions</div>
    </div>
    <div class="contact">
      <div><svg viewBox="0 0 24 24"><path d="M6.6 10.8a15.1 15.1 0 0 0 6.6 6.6l2.2-2.2a1 1 0 0 1 1-.25 11.4 11.4 0 0 0 3.6.57 1 1 0 0 1 1 1V20a1 1 0 0 1-1 1A17 17 0 0 1 3 4a1 1 0 0 1 1-1h3.5a1 1 0 0 1 1 1c0 1.25.2 2.45.57 3.57a1 1 0 0 1-.25 1z"/></svg>555-214-0937</div>
      <div><svg viewBox="0 0 24 24"><circle cx="12" cy="12" r="10"/></svg>www.brellix.com</div>
    </div>
  </header>

  <section class="hero" role="img" aria-label="Photo of a businessman touching a glowing digital world map interface">
    <p class="hero-tagline">When you have IT issues,<br><strong>we have IT SOLUTIONS.</strong></p>
  </section>

  <section class="intro">
    <h2>WHO WE ARE</h2>
    <p>Brellix is <span class="accent">a leading edge Information Technology (IT) services company</span> providing innovative solutions to all forms of IT challenges for small, medium and enterprise sized clients.</p>
    <p>Brellix has performed technology services in a multitude of industries including law enforcement, government, healthcare, educational, financial, broadcast and others. As a full service integrator, <span class="accent">Brellix provides network design, installation, maintenance, and administration.</span></p>
    <p>Whether you are a client who uses our Managed Services offerings or our Consulting Services, you can <span class="accent">expect Brellix’s certified professionals to achieve the best possible network performance, security and reliability</span> using the most expeditious and cost effective methods available.</p>
  </section>

  <section class="closing">
    <p>Free yourself up to focus on what’s important in<br>your business as you <span class="accent">turn over technology concerns to us.</span></p>
    <p>We provide <span class="accent">FREE</span> Personalized Assessment!</p>
    <svg width="829" height="70" viewBox="0 0 829 70" aria-hidden="true">
      <path d="M0 45 C 200 10, 500 70, 829 28 L829 70 L0 70 Z" fill="#a9cfea" opacity="0.6"/>
      <path d="M0 58 C 260 32, 520 78, 829 46 L829 70 L0 70 Z" fill="#1c7fc4" opacity="0.35"/>
    </svg>
  </section>
</main>
</body>
</html>
```